Redesign the *Settings* screen for the PelikoZ app.

PelikoZ app is in production, but we need to refresh and redesign the settings screen to be cleaner, easier, more intuitive, and more professional looking.

Project Deadline Extended
Reason: Several designers have requested more time. This will also give time to provide feedback on existing designs.

Requirements
Must have
• Black background, so that the screen is consistent with the rest of the app.

```html
<!DOCTYPE html>
<html lang="en">
<head>
<meta charset="utf-8">
<title>PelikoZ — Settings</title>
<link href="https://fonts.googleapis.com/css2?family=Montserrat:wght@400;500;600&display=swap" rel="stylesheet">
<style>
  :root {
    --canvas: #19222b;
    --screen: #232836;
    --tile: #2b3040;
    --tile-ink: #58607a;
    --ink: #ffffff;
    --ink-soft: #9aa2b8;
    --rule: #343a4b;
    --accent-a: #e4531d;
    --accent-b: #d8303c;
    --accent-solid: #e8552a;
    --tabbar: #1f2431;
  }
  * { box-sizing: border-box; margin: 0; padding: 0; }
  html, body { width: 1200px; height: 1200px; overflow: hidden; }
  body {
    background: var(--canvas);
    font-family: "Montserrat", Arial, sans-serif;
    color: var(--ink);
    position: relative;
  }
  .screen {
    position: absolute; left: 300px; top: 66px;
    width: 600px; height: 1068px;
    background: var(--screen);
    display: flex; flex-direction: column;
    overflow: hidden;
  }
  .status-bar {
    height: 44px; padding: 0 22px;
    display: flex; align-items: center; justify-content: space-between;
    font-size: 15px; font-weight: 500;
  }
  .status-bar .signal { display: flex; align-items: center; gap: 4px; }
  .dot { width: 8px; height: 8px; border-radius: 50%; border: 1px solid var(--ink); }
  .dot.on { background: var(--ink); }
  .status-bar .carrier { margin-left: 6px; }
  .status-bar .right { display: flex; align-items: center; gap: 10px; }
  .battery { width: 38px; height: 16px; border-radius: 3px; background: var(--ink); }

  .settings { padding: 20px 24px 0; display: flex; flex-direction: column; }
  .tile-row { display: flex; gap: 12px; }
  .tile {
    flex: 1; height: 84px; background: var(--tile); color: var(--tile-ink);
    display: flex; align-items: center; justify-content: center; gap: 22px;
    font-size: 20px; letter-spacing: 2px; text-transform: uppercase;
  }
  .tile.active {
    background: linear-gradient(100deg, var(--accent-a), var(--accent-b));
    color: var(--ink);
  }
  .tile svg { width: 44px; height: 44px; fill: none; stroke: currentColor; stroke-width: 2; stroke-linecap: round; stroke-linejoin: round; }
  .co2 { font-size: 24px; letter-spacing: 3px; }
  .co2 sub { font-size: 12px; }
  .field-label { font-size: 22px; font-weight: 500; margin: 26px 0 14px; }

  .logout-row { display: flex; justify-content: flex-end; margin-top: 20px; }
  .logout {
    background: var(--accent-solid); color: #f6c3a6;
    font-size: 16px; letter-spacing: 3px; padding: 12px 30px;
  }
  .profile { display: flex; align-items: center; gap: 26px; padding: 22px 0 26px; border-bottom: 1px solid var(--rule); }
  .avatar {
    width: 84px; height: 84px; border-radius: 50%;
    background: radial-gradient(circle at 45% 40%, #d99a7e, #7a5448 60%, #3c3c46);
  }
  .profile .name { font-size: 20px; letter-spacing: 3px; font-weight: 500; }
  .action { display: flex; align-items: center; gap: 30px; height: 76px; border-bottom: 1px solid var(--rule); color: var(--ink-soft); font-size: 18px; letter-spacing: 3px; }
  .action svg { width: 30px; height: 30px; fill: none; stroke: currentColor; stroke-width: 1.8; stroke-linecap: round; stroke-linejoin: round; }

  .tab-bar {
    margin-top: auto; height: 110px; background: var(--tabbar);
    display: flex; justify-content: space-around; align-items: center;
  }
  .tab { display: flex; flex-direction: column; align-items: center; gap: 10px; font-size: 14px; letter-spacing: 2px; color: var(--ink); }
  .tab svg { width: 40px; height: 40px; fill: none; stroke: currentColor; stroke-width: 2; stroke-linecap: round; stroke-linejoin: round; }
  .tab.current { color: var(--accent-solid); }
</style>
</head>
<body>
<main class="screen">
  <header class="status-bar">
    <div class="signal">
      <span class="dot on"></span><span class="dot on"></span><span class="dot"></span><span class="dot"></span><span class="dot"></span>
      <span class="carrier">Nimbus</span>
    </div>
    <div class="time">10:07 AM</div>
    <div class="right">
      <svg width="14" height="18" viewBox="0 0 14 18" fill="none" stroke="#fff" stroke-width="1.6"><path d="M2 5l10 8-5 4V1l5 4-10 8"/></svg>
      <span>68%</span>
      <span class="battery"></span>
    </div>
  </header>

  <section class="settings">
    <div class="tile-row">
      <div class="tile active"><svg viewBox="0 0 44 44"><rect x="10" y="19" width="24" height="18" rx="2"/><path d="M15 19v-5a7 7 0 0 1 14 0v5"/></svg></div>
      <div class="tile"><svg viewBox="0 0 44 44"><path d="M10 12h20v22H10z"/><path d="M14 8h20v22"/></svg></div>
      <div class="tile"><span class="co2">CO<sub>2</sub></span></div>
    </div>

    <h2 class="field-label">Device Mount Position</h2>
    <div class="tile-row">
      <div class="tile"><svg viewBox="0 0 44 44"><rect x="8" y="10" width="28" height="24" rx="1"/><path d="M16 22h14M24 16l6 6-6 6"/></svg>Forward</div>
      <div class="tile active"><svg viewBox="0 0 44 44"><rect x="8" y="10" width="28" height="24" rx="1"/><path d="M30 22H16M22 16l-6 6 6 6"/></svg>Backward</div>
    </div>

    <h2 class="field-label">Device Mount Location</h2>
    <div class="tile-row">
      <div class="tile active"><svg viewBox="0 0 44 44"><rect x="6" y="24" width="32" height="10" rx="5"/><circle cx="31" cy="29" r="2"/><path d="M11 29h12M18 8v10M14 14l4 4 4-4"/></svg></div>
      <div class="tile"><svg viewBox="0 0 44 44"><rect x="6" y="24" width="32" height="10" rx="5"/><circle cx="31" cy="29" r="2"/><path d="M11 29h12M18 18V8M14 12l4-4 4 4"/></svg></div>
      <div class="tile"><svg viewBox="0 0 44 44"><rect x="6" y="24" width="32" height="10" rx="5"/><circle cx="31" cy="29" r="2"/><path d="M11 29h12M26 13H12M16 9l-4 4 4 4"/></svg></div>
      <div class="tile"><svg viewBox="0 0 44 44"><rect x="6" y="24" width="32" height="10" rx="5"/><circle cx="31" cy="29" r="2"/><path d="M11 29h12M14 13h14M24 9l4 4-4 4"/></svg></div>
    </div>

    <h2 class="field-label">Bullseye Mode</h2>
    <div class="tile-row">
      <div class="tile"><svg viewBox="0 0 44 44"><circle cx="22" cy="22" r="15"/><circle cx="22" cy="22" r="8"/><path d="M22 22l6-10"/></svg>On</div>
      <div class="tile active"><svg viewBox="0 0 44 44"><circle cx="22" cy="22" r="15"/><circle cx="22" cy="22" r="9"/><circle cx="22" cy="22" r="3"/><path d="M22 22l6-10"/></svg>Off</div>
    </div>

    <div class="logout-row"><span class="logout">LOGOUT</span></div>

    <div class="profile">
      <div class="avatar" role="img" aria-label="Profile photo of the signed-in user"></div>
      <span class="name">JONAH</span>
    </div>
    <div class="action">
      <svg viewBox="0 0 30 30"><path d="M6 13a9 9 0 0 1 16-5l2 2M24 17a9 9 0 0 1-16 5l-2-2"/><path d="M24 5v5h-5M6 25v-5h5"/></svg>
      SYNC ACCOUNT DATA
    </div>
    <div class="action">
      <svg viewBox="0 0 30 30"><path d="M9 9l12 10-6 5V6l6 5L9 21"/></svg>
      DISCONNECT BLUETOOTH
    </div>
  </section>

  <nav class="tab-bar">
    <div class="tab"><svg viewBox="0 0 40 40"><circle cx="20" cy="20" r="13"/><circle cx="20" cy="20" r="4" fill="currentColor"/><path d="M20 4v6M20 30v6M4 20h6M30 20h6"/></svg>TRAIN</div>
    <div class="tab"><svg viewBox="0 0 40 40"><path d="M5 34h30M8 34V22h7v12M16 34V14h7v20M24 34V8h7v26"/></svg>HISTORY</div>
    <div class="tab"><svg viewBox="0 0 40 40"><path d="M3 16l17-8 17 8-17 8z"/><path d="M10 19v8c4 4 16 4 20 0v-8M35 17v10"/></svg>LEARN</div>
    <div class="tab current"><svg viewBox="0 0 40 40"><circle cx="20" cy="20" r="5"/><path d="M17 4h6l1 5 4 2 4-3 4 4-3 4 2 4 5 1v6l-5 1-2 4 3 4-4 4-4-3-4 2-1 5h-6l-1-5-4-2-4 3-4-4 3-4-2-4-5-1v-6l5-1 2-4-3-4 4-4 4 3 4-2z"/></svg>SETTINGS</div>
  </nav>
</main>
</body>
</html>
```